South Florida Real Estate Brokerage Business

The name is HOME CALVINA REAL ESTATE.
The company is a Real estate realty based in Miami.
Is targeted to Latin American clients.
Must express luxury, and efficiency.
Target clients for properties around 250k to a million +.
Calvina means Royal in Latin.
Should communicate safety and knowledge of the product and transaction with a tech edge.

The web design needs to be a Social tool, with Friendlane and other media integration of some sort. Needs to have a Show case place, a Search place (MLS listings) with maps and filters.
Needs to reflect luxury but also mixed with a social edge capable of engaging clients or transition them to communicate with the page.
Include the logo from the uploaded files, feel free to change the color or font per webdesign.
This is a Front en design, layout and graphics.
Possible future programming if approved.
I can receive Quotes for the Code part.

Target Market(s)

Spanish and English speakers living in Latin America and Canada looking for apartments and houses to buy.

Industry/Entity Type

Business

Requirements
Must have
• Search area.
Neighbourhood area.
Could be a blog or news area.
Client registration.
Social Plugin
Nice to have
• Social linking to networks.
Log in with friendlane account.
Friendlane Like.

```html
<!DOCTYPE html>
<html lang="en">
<head>
<meta charset="utf-8">
<title>Home Calvina Real Estate</title>
<link href="https://fonts.googleapis.com/css2?family=Marcellus&family=Open+Sans:ital,wght@0,400;0,600;0,700;1,400&display=swap" rel="stylesheet">
<style>
:root{
  --gold:#b59a74;
  --ink:#1e1e1e;
  --muted:#555;
  --line:#d9d9d9;
  --quote:#c8c8c8;
  --panel:rgba(40,30,45,.88);
  --copper:#b5682f;
  --red:#c8141a;
  --green:#4c9a1c;
  --footer:#222;
  --bg:#ffffff;
}
*{box-sizing:border-box;margin:0;padding:0}
html,body{width:1200px;height:1162px;overflow:hidden;background:var(--bg)}
body{position:relative;font-family:"Open Sans",Arial,sans-serif;color:var(--ink)}
.abs{position:absolute}

/* header */
.brand{left:108px;top:0;width:174px;height:106px;background:#fff;box-shadow:0 2px 6px rgba(0,0,0,.15);z-index:3;display:flex;align-items:center;gap:10px;padding:0 14px}
.brand-mark{flex:none;width:28px;height:28px;background:var(--gold)}
.brand-name{font-family:"Open Sans",Arial,sans-serif;font-weight:600;color:var(--ink);font-size:13px;line-height:17px;letter-spacing:.5px}
.nav{top:26px;left:0;font-family:"Marcellus",serif;font-size:13px}
.nav a{position:absolute;white-space:nowrap;color:var(--ink);text-decoration:none}
.nav a.active{color:var(--gold)}
.call{left:930px;top:11px;font-family:"Marcellus",serif;font-size:13px;font-weight:bold}
.phone{left:864px;top:27px;font-family:"Marcellus",serif;font-size:22px;color:var(--gold)}

/* hero */
.hero{left:89px;top:60px;width:1022px;height:564px;background:linear-gradient(180deg,#7a2c8c 0%,#9c3a9a 25%,#3d2a55 55%,#1f2a4a 100%);box-shadow:0 2px 8px rgba(0,0,0,.3)}
.hero-copy{left:0;top:300px;width:533px;height:264px;background:rgba(245,238,225,.55);padding:30px 40px 0 20px}
.hero-title{font-family:"Marcellus",serif;font-weight:normal;font-size:32px;color:#fff;text-shadow:0 1px 3px rgba(0,0,0,.5);margin-bottom:12px;white-space:nowrap}
.hero-text{font-style:italic;font-size:14px;line-height:15.4px;color:#111;margin-bottom:15px}
.thumbs{top:502px;left:687px}
.thumb{position:absolute;top:0;width:58px;height:50px;border:2px solid #eee}
.search{left:755px;top:20px;width:254px;height:338px;background:var(--panel);border-top:4px solid var(--gold);color:#fff;padding:14px 15px}
.search h2{font-family:"Marcellus",serif;font-weight:normal;font-size:18px;margin-bottom:12px}
.radios{font-family:"Marcellus",serif;font-size:13px;display:flex;gap:46px;margin-bottom:14px}
.radio{display:inline-block;width:9px;height:9px;border-radius:50%;background:#fff;margin-right:6px;border:2px solid #fff}
.radio.on{border-color:#9cf;background:#357}
.field{display:flex;align-items:center;height:37.5px;font-family:"Marcellus",serif;font-size:11px;letter-spacing:.3px}
.field span{width:110px}
.select{height:18px;background:#fff;color:#000;font-family:Arial,sans-serif;font-size:10.5px;padding:2px 4px;position:relative}
.select::after{content:"";position:absolute;right:1px;top:1px;width:13px;height:14px;background:#ddd;border:1px solid #888}
.btn-search{position:absolute;right:20px;bottom:14px;width:70px;height:22px;background:var(--copper);font-family:"Marcellus",serif;font-size:11px;text-align:center;line-height:22px}

/* blogs */
.blog-title{left:116px;top:652px;font-family:"Marcellus",serif;font-size:14px;font-weight:bold;display:flex;align-items:center;gap:10px}
.bubble{width:44px;height:30px}
.blog{left:116px;width:274px;border-bottom:1px solid var(--line);padding:0 0 8px 10px;font-size:11px;line-height:15.5px;color:var(--muted)}
.blog p{font-style:italic;text-indent:18px}
.blog .open{position:absolute;left:-2px;top:-6px;font-family:"Marcellus",serif;color:var(--quote);font-size:36px;line-height:36px}
.blog .close{font-family:"Marcellus",serif;color:var(--quote);font-size:36px;line-height:14px;height:14px;padding-left:82px;overflow:visible}
.blog .by{color:var(--ink);font-style:italic;margin-top:2px}
.view-all{left:344px;top:981px;color:var(--gold);font-family:"Marcellus",serif;font-size:12px}

/* neighbourhood */
.section-title{font-family:"Marcellus",serif;font-size:13px;font-weight:bold;white-space:nowrap}
.map{left:434px;top:691px;width:328px;height:244px;background:linear-gradient(135deg,#7b7c64,#9a9983 50%,#6f7560)}

/* registration */
.reg{left:816px;top:662px;width:282px;height:300px;background:linear-gradient(#fafafa,#e8e8e8);box-shadow:0 8px 10px -6px rgba(0,0,0,.45)}
.reg-head{left:802px;top:662px;width:308px;height:40px;background:linear-gradient(#d6242a,#a80e12);color:#fff;font-family:"Marcellus",serif;font-weight:normal;font-size:20px;text-align:center;line-height:40px}
.input{left:848px;width:214px;height:37px;border:1px solid #ccc;border-radius:16px;background:#fff;font-size:11px;color:#444;padding-left:14px;line-height:35px}
.register{left:906px;top:900px;width:112px;height:28px;background:linear-gradient(#6cbf2c,var(--green));color:#fff;font-family:"Marcellus",serif;font-size:14px;text-align:center;line-height:28px;border-radius:3px}
.reg-arrow{left:900px;top:906px}

/* partners */
.partners{left:168px;top:1032px;height:48px;display:flex}
.partner{width:144px;height:48px;border-left:1px solid var(--line);display:flex;align-items:center;justify-content:center;font-family:"Marcellus",serif;font-size:23px;color:#8a8a8a}
.partner:first-child{border-left:none;color:#111}
.partner-bar{left:168px;top:1094px;width:144px;height:4px;background:#d04a1a}

/* footer */
.footer{left:0;top:1098px;width:1200px;height:64px;background:var(--footer)}
.foot-brand{left:176px;top:1108px;display:flex;align-items:center;gap:6px;font-family:"Open Sans",Arial,sans-serif;font-weight:600;color:#888;font-size:10px}
.foot-mark{width:16px;height:16px;background:#6a5a40}
.privacy{left:300px;top:1112px;color:#fff;font-size:8.5px;font-weight:700}
.social{left:938px;top:1106px;display:flex;gap:4px}
.social i{display:block;width:11px;height:11px;background:#777}
</style>
</head>
<body>

<header>
  <div class="abs brand">
    <div class="brand-mark"></div>
    <div class="brand-name">HOME CALVINA REAL ESTATE</div>
  </div>
  <nav class="abs nav">
    <a class="active" style="left:318px">HOME</a>
    <a style="left:390px">ABOUT US</a>
    <a style="left:485px">SERVICES</a>
    <a style="left:571px">FOLIO</a>
    <a style="left:643px">OFFERS</a>
    <a style="left:720px">CONTACT US</a>
  </nav>
  <div class="abs call">CALL NOW:</div>
  <div class="abs phone">+00 (1) 555 010 2480</div>
</header>

<section class="abs hero" role="img" aria-label="Night view of a waterfront city skyline with hotel towers under a purple sky">
  <div class="abs hero-copy">
    <h1 class="hero-title">ROYAL, LUXURY, AND EFFICIENCY.</h1>
    <p class="hero-text">Lorem Ipsum is simply dummy text of the printing and typesetting industry. Lorem Ipsum has been the industry's standard dummy text ever since the 1500s, when an unknown printer took a galley of type and scrambled it to make a type specimen book.</p>
    <p class="hero-text">It has survived not only five centuries, but also the leap into electronic typesetting, remaining essentially unchanged. It was popularised in the 1960s with the release of printed sheets containing Lorem Ipsum passages, and more recently with desktop publishing software including versions of Lorem Ipsum.</p>
  </div>

  <form class="abs search">
    <h2>SEARCH</h2>
    <div class="radios"><span><i class="radio on"></i>FOR SALE</span><span><i class="radio"></i>FOR RENT</span></div>
    <div class="field"><span>PROPERTY TYPE</span><div class="select" style="width:98px">Condominiums</div></div>
    <div class="field"><span>CITY NAME</span><div class="select" style="width:98px">Miami Beach</div></div>
    <div class="field"><span>PRICE MIN</span><div class="select" style="width:76px">$250,000</div></div>
    <div class="field"><span>PRICE MAX</span><div class="select" style="width:76px">$5 M+</div></div>
    <div class="field"><span>BEDS ROOMS</span><div class="select" style="width:46px">1+</div></div>
    <div class="field"><span>BATHS ROOMS</span><div class="select" style="width:46px">1+</div></div>
    <div class="btn-search">SEARCH</div>
  </form>

  <div class="abs thumbs">
    <div class="thumb" style="left:0;background:linear-gradient(#8a3a9a,#2a2a55)" role="img" aria-label="City skyline thumbnail"></div>
    <div class="thumb" style="left:65px;background:linear-gradient(#8fb4d8,#dfe8f0)" role="img" aria-label="Running horse thumbnail"></div>
    <div class="thumb" style="left:131px;background:linear-gradient(#6f9fd0,#9a8a78)" role="img" aria-label="Tower building thumbnail"></div>
    <div class="thumb" style="left:196px;background:linear-gradient(#7a1010,#c82020)" role="img" aria-label="Red lounge interior thumbnail"></div>
    <div class="thumb" style="left:262px;background:linear-gradient(#9ec4e4,#3a7aa8)" role="img" aria-label="Harbour view thumbnail"></div>
  </div>
</section>

<section>
  <div class="abs blog-title">
    <svg class="bubble" viewBox="0 0 44 30"><path d="M4 2h22a4 4 0 0 1 4 4v10a4 4 0 0 1-4 4H12l-6 6v-6H4a4 4 0 0 1-4-4V6a4 4 0 0 1 4-4z" fill="#333"/><path d="M20 10h20a4 4 0 0 1 4 4v8a4 4 0 0 1-4 4h-2v4l-5-4H20a4 4 0 0 1-4-4v-8a4 4 0 0 1 4-4z" fill="#555"/><circle cx="26" cy="18" r="1.5" fill="#fff"/><circle cx="31" cy="18" r="1.5" fill="#fff"/><circle cx="36" cy="18" r="1.5" fill="#fff"/></svg>
    OUR RECENT BLOGS
  </div>
  <article class="abs blog" style="top:690px">
    <span class="open">&ldquo;</span>
    <p>Lorem Ipsum is simply dummy text of the printing and typesetting industry. Lorem Ipsum has been the industry's standard dummy text ever since the 1500s,</p>
    <div class="close">&rdquo;</div>
    <div class="by">Lorem Ipsum. , Miami...</div>
  </article>
  <article class="abs blog" style="top:792px">
    <span class="open">&ldquo;</span>
    <p>Lorem Ipsum is simply dummy text of the printing and typesetting industry. Lorem Ipsum has been the industry's standard dummy text ever since the 1500s,</p>
    <div class="close">&rdquo;</div>
    <div class="by">Lorem Ipsum. , Miami...</div>
  </article>
  <article class="abs blog" style="top:896px;border-bottom:none">
    <span class="open">&ldquo;</span>
    <p>Lorem Ipsum is simply dummy text of the printing and typesetting industry. Lorem Ipsum has been the industry's standard dummy text ever since the 1500s,</p>
    <div class="close">&rdquo;</div>
    <div class="by">Lorem Ipsum. , Miami...</div>
  </article>
  <div class="abs view-all">View All</div>
</section>

<section>
  <h3 class="abs section-title" style="left:434px;top:660px">NEIGHBOURHOOD AREA</h3>
  <div class="abs map" role="img" aria-label="Aerial map of a Miami neighbourhood with a highway and street grid"></div>
  <h3 class="abs section-title" style="left:454px;top:950px">SEARCH YOU NEIGHOURHOOD AREA HERE</h3>
</section>

<section>
  <div class="abs reg"></div>
  <h3 class="abs reg-head">Client Registration</h3>
  <div class="abs input" style="top:718px">Enter User Name...</div>
  <div class="abs input" style="top:761px">Password...</div>
  <div class="abs input" style="top:804px">Phone number...</div>
  <div class="abs input" style="top:847px">Email Address...</div>
  <div class="abs register">Register</div>
  <svg class="abs reg-arrow" width="26" height="20" viewBox="0 0 26 20"><path d="M0 6h14V0l12 10-12 10v-6H0z" fill="#c81a1a"/></svg>
</section>

<section class="abs partners">
  <div class="partner">NORVELL</div>
  <div class="partner">Tilecrest</div>
  <div class="partner">SWIFTA</div>
  <div class="partner">CITRINE</div>
  <div class="partner">VAULTA</div>
  <div class="partner">Mosaic</div>
</section>
<div class="abs partner-bar"></div>

<footer>
  <div class="abs footer"></div>
  <div class="abs foot-brand"><div class="foot-mark"></div>HOME CALVINA</div>
  <div class="abs privacy">PRIVACY POLICY</div>
  <div class="abs social"><i></i><i></i><i></i><i></i></div>
</footer>

</body>
</html>
```